Presentation Template for Copperleaf Studio

We would like to have a template for our presentations since we have a new logo and want a new general image.

The new template should have as minimum Cover/Title Page, Bullets page and Regular page. We have a new logo and need the template to mach with it. For the bullets and regular page we want the design no take much part for including content, so we would like something that makes the slides look good but leaving most of room free for writing.

We would like the logo on the footer of the regular slides (not of course for the cover, dividers etc)

I'm attaching de logo here. Our logo colours are #b80016, #006ac6 and black

Thank you

Industry/Entity Type

It Company

Font styles to use
Other font styles liked:
• Maven Pro

Colors
ec1f27
0355a3
000000

Requirements
Must have
• Presentation template with Cover/Title Page, Bullets page and Regular page. Must match with our new logo.
• We would like the logo on the footer of the regular slides (not of course for the cover, dividers etc)
• Our logo colours are #b80016, #006ac6 and black
Nice to have
• Other type of slides, special bullets etc
Should not have
• I don't know

```html
<!DOCTYPE html>
<html lang="en">
<head>
<meta charset="utf-8">
<title>Copperleaf Studio – Presentation Template</title>
<link href="https://fonts.googleapis.com/css2?family=Maven+Pro:wght@400;500;600;700&display=swap" rel="stylesheet">
<style>
:root{
  --blue:#0a63c9;
  --blue-2:#1e72d2;
  --blue-dark:#0b4fa8;
  --red:#c0121f;
  --black:#111111;
  --ink:#222222;
  --gray:#8a8a8a;
  --light:#f2f4f7;
  --white:#ffffff;
}
*{box-sizing:border-box;margin:0;padding:0}
html,body{width:1053px;height:1200px;overflow:hidden;background:var(--white)}
body{position:relative;font-family:"Maven Pro",Arial,sans-serif;color:var(--ink)}
.slide{position:absolute;width:344px;height:192px;overflow:hidden;background:var(--white);box-shadow:0 0 0 1px #e6e8ec}
.abs{position:absolute}
.photo{position:absolute}
.col-a{left:4px}.col-b{left:355px}.col-c{left:705px}
.row-1{top:2px}.row-2{top:201px}.row-3{top:400px}.row-4{top:598px}.row-5{top:797px}.row-6{top:996px}

.brand{position:absolute;display:flex;align-items:center;gap:3px;font-weight:600;text-transform:uppercase;letter-spacing:.08em;white-space:nowrap;line-height:1}
.brand .mark{display:inline-block;background:currentColor}
.brand--red{color:var(--red)}
.brand--white{color:var(--white)}

.title{position:absolute;left:19px;top:18px;font-size:14px;font-weight:400;letter-spacing:.02em;text-transform:uppercase;color:var(--ink)}
.title::after{content:"";position:absolute;left:0;bottom:-4px;width:22px;height:2px;background:var(--red)}

.cover-title{font-weight:600;text-transform:uppercase;letter-spacing:.03em;line-height:1.1}
.sub{font-size:5px;letter-spacing:.03em}
.tiny{font-size:3.6px;line-height:1.35}
.small{font-size:5.5px;line-height:1.25}

.foot{position:absolute;left:0;right:0;bottom:0;height:10px}
.foot .band{position:absolute;left:30px;right:0;bottom:0;height:5px;background:var(--blue);clip-path:polygon(6px 0,100% 0,100% 100%,0 100%)}
.foot .brand{left:5px;bottom:2px;font-size:3.4px}
.foot .brand .mark{width:3px;height:3px}
.foot .copy{position:absolute;right:14px;bottom:1px;font-size:2.8px;color:var(--white)}
.foot .page{position:absolute;right:4px;bottom:1px;font-size:2.8px;color:var(--white)}

/* agenda */
.agenda-item{position:absolute;width:130px;height:20px}
.agenda-item .time{position:absolute;left:0;top:2px;width:27px;height:9px;background:var(--blue);color:var(--white);font-size:3.6px;display:flex;align-items:center;justify-content:space-between;padding:0 3px}
.agenda-item .time i{display:inline-block;width:5px;height:5px;border:0.8px solid var(--white);border-radius:50%}
.agenda-item h4{position:absolute;left:36px;top:1px;font-size:6px;font-weight:500;color:var(--blue)}
.agenda-item p{position:absolute;left:36px;top:9px;width:90px;color:var(--gray)}

/* info cells */
.cell{position:absolute;color:var(--white);padding:6px 9px}
.cell--blue{background:var(--blue)}
.cell--red{background:var(--red)}
.cell--black{background:var(--black)}
.cell h5{font-size:6px;font-weight:500;margin-bottom:3px}

.feature{position:absolute;color:var(--white);text-align:center;padding:0 6px}
.feature svg{display:block;margin:0 auto}
.feature h5{font-size:5.5px;font-weight:500;margin:8px 0 3px}

.bullet{position:absolute;width:100px;height:20px}
.bullet .dot{position:absolute;left:0;top:0;width:11px;height:11px;border-radius:50%}
.bullet h6{position:absolute;left:18px;top:0;font-size:5px;font-weight:500}
.bullet p{position:absolute;left:18px;top:7px;color:var(--gray)}

.label{position:absolute;width:40px;height:12px;color:var(--white);font-size:3.4px;line-height:1.15;padding:1.5px 3px}

.btn{position:absolute;background:var(--blue);color:var(--white);font-size:4px;padding:3px 10px;letter-spacing:.04em}
</style>
</head>
<body>

<!-- Row 1 -->
<section class="slide col-a row-1" aria-label="Cover slide, blue">
  <div class="photo" role="img" aria-label="Blue-tinted photo of a modern office tower facade" style="inset:0;background:linear-gradient(135deg,#3d8ae0 0%,#0b55b0 45%,#1c6dc9 75%,#0a4a9c 100%)"></div>
  <div class="brand brand--white" style="left:93px;top:84px;font-size:11px"><span class="mark" style="width:10px;height:10px"></span>Copperleaf Studio</div>
  <div class="abs cover-title" style="left:0;right:0;top:130px;text-align:center;color:var(--white);font-size:14px">Your Title Goes Here</div>
  <div class="abs sub" style="left:0;right:0;top:147px;text-align:center;color:var(--white)">Your Subtitle Goes Here</div>
</section>

<section class="slide col-b row-1" aria-label="Cover slide with presenters">
  <div class="brand brand--red" style="left:22px;top:16px;font-size:8px"><span class="mark" style="width:8px;height:8px"></span>Copperleaf Studio</div>
  <div class="photo" role="img" aria-label="Low-angle photo of skyscrapers with warm sunlight" style="left:0;right:0;top:30px;height:118px;background:linear-gradient(160deg,#fff4dc 0%,#f1c27a 25%,#b98a55 50%,#6d7890 80%,#3d5577 100%)"></div>
  <div class="abs" style="left:0;right:0;top:108px;height:40px;background:rgba(10,99,201,.85)"></div>
  <div class="abs cover-title" style="left:0;right:0;top:117px;text-align:center;color:var(--white);font-size:12px;font-weight:400">Your Title Goes Here</div>
  <div class="abs sub" style="left:0;right:0;top:131px;text-align:center;color:var(--white);font-size:4.5px">Your Subtitle Goes Here</div>
  <div class="abs" style="left:4px;top:179px;font-size:2.8px;color:var(--gray)">Presented by</div>
  <div class="abs" style="left:27px;top:176px;font-size:4px;color:var(--blue)">&#9679; Alan Reed<br><span style="font-size:2.6px;color:var(--gray)">Head of Sales</span></div>
  <div class="abs" style="left:83px;top:176px;font-size:4px;color:var(--blue)">&#9679; Mara Lin<br><span style="font-size:2.6px;color:var(--gray)">Lead Consultant</span></div>
  <div class="abs" style="left:146px;top:174px;width:1px;height:12px;background:#cfd4da"></div>
  <div class="abs" style="left:168px;top:179px;font-size:2.8px;color:var(--gray)">Hosted by</div>
  <div class="abs" style="left:190px;top:176px;font-size:4px;color:var(--blue)">&#9679; Owen Hale<br><span style="font-size:2.6px;color:var(--gray)">Vice President</span></div>
  <div class="abs" style="right:4px;top:179px;font-size:3.2px;color:var(--gray)">Cityname | November 28, 2017</div>
</section>

<section class="slide col-c row-1" aria-label="Cover slide with red panel">
  <div class="photo" role="img" aria-label="Pale gray photo of glass architecture" style="inset:0;background:linear-gradient(120deg,#e9ecf0,#f7f8fa 50%,#dfe3e8)"></div>
  <div class="photo" role="img" aria-label="Red-tinted city street photo" style="left:0;top:0;width:255px;height:120px;background:linear-gradient(135deg,#d8323c,#b10f1b 55%,#8e0a14)"></div>
  <div class="abs" style="left:0;top:0;width:40px;height:120px;background:var(--blue)"></div>
  <div class="brand brand--red" style="right:12px;top:138px;font-size:6px"><span class="mark" style="width:6px;height:6px"></span>Copperleaf Studio</div>
  <div class="abs cover-title" style="right:12px;top:160px;color:var(--blue);font-size:14px">Your Title Goes Here</div>
  <div class="abs sub" style="right:12px;top:176px;color:var(--blue)">Your Subtitle Goes Here</div>
</section>

<!-- Row 2 -->
<section class="slide col-a row-2" aria-label="Cover slide with city photo">
  <div class="photo" role="img" aria-label="Black and white aerial photo of a city skyline under a blue overlay" style="inset:0;background:linear-gradient(100deg,#0d55ad 0%,#1467c6 30%,#5c6670 55%,#2a2f35 100%)"></div>
  <div class="brand brand--red" style="right:16px;top:133px;font-size:6px"><span class="mark" style="width:6px;height:6px"></span>Copperleaf Studio</div>
  <div class="abs cover-title" style="right:14px;top:158px;color:var(--white);font-size:14px">Your Title Goes Here</div>
  <div class="abs sub" style="right:14px;top:174px;color:var(--white)">Your Subtitle Goes Here</div>
</section>

<section class="slide col-b row-2" aria-label="Agenda slide">
  <h2 class="title">Our Agenda</h2>
  <div class="agenda-item" style="left:30px;top:56px"><div class="time">10:00<i></i></div><h4>Agenda One</h4><p class="tiny">Brief note about this item.</p></div>
  <div class="agenda-item" style="left:30px;top:92px"><div class="time">11:00<i></i></div><h4>Agenda Two</h4><p class="tiny">Brief note about this item.</p></div>
  <div class="agenda-item" style="left:30px;top:136px"><div class="time">12:00<i></i></div><h4>Agenda Three</h4><p class="tiny">Brief note about this item.</p></div>
  <div class="agenda-item" style="left:172px;top:56px"><div class="time">13:00<i></i></div><h4>Agenda Four</h4><p class="tiny">Brief note about this item.</p></div>
  <div class="agenda-item" style="left:172px;top:92px"><div class="time">14:00<i></i></div><h4>Agenda Five</h4><p class="tiny">Brief note about this item.</p></div>
  <div class="agenda-item" style="left:172px;top:136px"><div class="time">15:00<i></i></div><h4>Agenda Six</h4><p class="tiny">Brief note about this item.</p></div>
  <div class="foot"><div class="brand brand--red"><span class="mark"></span>Copperleaf Studio</div><div class="band"></div><span class="copy">© 2017 Copperleaf Studio. All rights reserved</span><span class="page">5</span></div>
</section>

<section class="slide col-c row-2" aria-label="Text and picture grid">
  <div class="cell cell--blue tiny" style="left:0;top:0;width:172px;height:58px;padding-top:10px">Use this space for a short summary of the key message, supporting facts and a clear next step for the team.</div>
  <div class="photo" role="img" aria-label="Photo of steel and glass roof structure" style="left:172px;top:0;width:172px;height:58px;background:linear-gradient(135deg,#9aa3ad,#4c5560 50%,#c8ced5)"></div>
  <div class="photo" role="img" aria-label="Photo of a city skyline at sunset" style="left:0;top:58px;width:172px;height:74px;background:linear-gradient(180deg,#e9d6b8,#b39a7c 45%,#5a5550)"></div>
  <div class="cell cell--red tiny" style="left:172px;top:58px;width:172px;height:74px;padding-top:18px">Use this space for a short summary of the key message, supporting facts and a clear next step for the team.</div>
  <div class="cell cell--black tiny" style="left:0;top:132px;width:172px;height:60px;padding-top:10px">Use this space for a short summary of the key message, supporting facts and a clear next step for the team.</div>
  <div class="photo" role="img" aria-label="Blue-gray photo of a modern building interior" style="left:172px;top:132px;width:172px;height:60px;background:linear-gradient(135deg,#dfe6ee,#a9b8c8 50%,#e9eef3)"></div>
</section>

<!-- Row 3 -->
<section class="slide col-a row-3" aria-label="Four column features">
  <h2 class="title">Your Title Here</h2>
  <div class="feature cell--blue" style="left:0;top:66px;width:86px;height:96px;padding-top:12px">
    <svg width="16" height="16" viewBox="0 0 16 16" fill="none" stroke="#fff" stroke-width="1"><circle cx="8" cy="8" r="6.5"/><ellipse cx="8" cy="8" rx="3" ry="6.5"/><line x1="1.5" y1="8" x2="14.5" y2="8"/></svg>
    <h5>Heading Here</h5><p class="tiny">Add a short description of this point in a few simple words here.</p></div>
  <div class="feature cell--red" style="left:86px;top:66px;width:86px;height:96px;padding-top:12px">
    <svg width="16" height="16" viewBox="0 0 16 16" fill="none" stroke="#fff" stroke-width="1"><circle cx="8" cy="6.5" r="4.5"/><line x1="6" y1="12" x2="10" y2="12"/><line x1="6.5" y1="14" x2="9.5" y2="14"/></svg>
    <h5>Heading Here</h5><p class="tiny">Add a short description of this point in a few simple words here.</p></div>
  <div class="feature cell--blue" style="left:172px;top:66px;width:86px;height:96px;padding-top:12px">
    <svg width="16" height="16" viewBox="0 0 16 16" fill="none" stroke="#fff" stroke-width="1"><circle cx="8" cy="8" r="3"/><circle cx="3" cy="3" r="1.5"/><circle cx="13" cy="3" r="1.5"/><circle cx="3" cy="13" r="1.5"/><circle cx="13" cy="13" r="1.5"/></svg>
    <h5>Heading Here</h5><p class="tiny">Add a short description of this point in a few simple words here.</p></div>
  <div class="feature cell--red" style="left:258px;top:66px;width:86px;height:96px;padding-top:12px">
    <svg width="16" height="16" viewBox="0 0 16 16" fill="none" stroke="#fff" stroke-width="1"><rect x="2" y="2" width="12" height="10"/><line x1="4" y1="5" x2="12" y2="5"/><line x1="4" y1="8" x2="10" y2="8"/><line x1="6" y1="14" x2="10" y2="14"/></svg>
    <h5>Heading Here</h5><p class="tiny">Add a short description of this point in a few simple words here.</p></div>
  <div class="foot"><div class="brand brand--red"><span class="mark"></span>Copperleaf Studio</div><div class="band"></div><span class="copy">© 2017 Copperleaf Studio. All rights reserved</span><span class="page">7</span></div>
</section>

<section class="slide col-b row-3" aria-label="Divider page" style="background:var(--blue)">
  <div class="abs" style="left:0;top:0;width:120px;height:192px;background:linear-gradient(90deg,rgba(255,255,255,.06),rgba(255,255,255,0))"></div>
  <div class="abs cover-title" style="right:18px;top:134px;color:var(--white);font-size:14px">Divider Page</div>
  <div class="abs sub" style="right:18px;top:150px;color:var(--white);font-size:5.5px">Subtitle Here</div>
  <p class="abs tiny" style="right:18px;top:160px;width:130px;text-align:right;color:var(--white)">Use this line to introduce the next section of the deck with a brief summary.</p>
</section>

<section class="slide col-c row-3" aria-label="Text and bullet area">
  <h2 class="title">Text &amp; Bullet Area</h2>
  <div class="abs" style="left:19px;top:58px;width:90px">
    <h5 style="font-size:5.5px;font-weight:500;margin-bottom:6px">Heading Goes Here</h5>
    <p class="tiny" style="color:var(--gray);margin-bottom:5px">Write a short paragraph that explains the topic in plain words.</p>
    <p class="tiny" style="color:var(--gray);margin-bottom:5px">Write a short paragraph that explains the topic in plain words.</p>
    <p class="tiny" style="color:var(--gray)">Write a short paragraph that explains the topic in plain words.</p>
  </div>
  <div class="bullet" style="left:128px;top:58px"><span class="dot" style="background:var(--blue)"></span><h6 style="color:var(--blue)">Your Text Here</h6><p class="tiny">Short supporting detail.</p></div>
  <div class="bullet" style="left:128px;top:86px"><span class="dot" style="background:var(--red)"></span><h6 style="color:var(--red)">Your Text Here</h6><p class="tiny">Short supporting detail.</p></div>
  <div class="bullet" style="left:128px;top:114px"><span class="dot" style="background:var(--blue)"></span><h6 style="color:var(--blue)">Your Text Here</h6><p class="tiny">Short supporting detail.</p></div>
  <div class="bullet" style="left:128px;top:142px"><span class="dot" style="background:var(--red)"></span><h6 style="color:var(--red)">Your Text Here</h6><p class="tiny">Short supporting detail.</p></div>
  <div class="bullet" style="left:236px;top:58px"><span class="dot" style="background:var(--red)"></span><h6 style="color:var(--red)">Your Text Here</h6><p class="tiny">Short supporting detail.</p></div>
  <div class="bullet" style="left:236px;top:86px"><span class="dot" style="background:var(--blue)"></span><h6 style="color:var(--blue)">Your Text Here</h6><p class="tiny">Short supporting detail.</p></div>
  <div class="bullet" style="left:236px;top:114px"><span class="dot" style="background:var(--red)"></span><h6 style="color:var(--red)">Your Text Here</h6><p class="tiny">Short supporting detail.</p></div>
  <div class="bullet" style="left:236px;top:142px"><span class="dot" style="background:var(--blue)"></span><h6 style="color:var(--blue)">Your Text Here</h6><p class="tiny">Short supporting detail.</p></div>
  <div class="foot"><div class="brand brand--red"><span class="mark"></span>Copperleaf Studio</div><div class="band"></div><span class="copy">© 2017 Copperleaf Studio. All rights reserved</span><span class="page">9</span></div>
</section>

<!-- Row 4 -->
<section class="slide col-a row-4" aria-label="Five step columns">
  <div class="feature" style="left:0;top:0;width:69px;height:192px;padding-top:44px;background:var(--blue)">
    <svg width="22" height="22" viewBox="0 0 22 22" fill="none" stroke="#fff" stroke-width="1"><circle cx="11" cy="11" r="6"/><circle cx="11" cy="11" r="2.5"/><path d="M11 2v3M11 17v3M2 11h3M17 11h3"/></svg>
    <h5 style="margin-top:34px">Heading Here</h5><p class="tiny" style="text-align:left">Describe this step in a few short and clear words for the audience.</p></div>
  <div class="feature" style="left:69px;top:0;width:69px;height:192px;padding-top:44px;background:var(--blue-2)">
    <svg width="22" height="22" viewBox="0 0 22 22" fill="none" stroke="#fff" stroke-width="1"><rect x="3" y="3" width="16" height="11"/><path d="M6 11l3-3 3 2 4-4M11 14v4M7 20l4-2 4 2"/></svg>
    <h5 style="margin-top:34px">Heading Here</h5><p class="tiny" style="text-align:left">Describe this step in a few short and clear words for the audience.</p></div>
  <div class="feature" style="left:138px;top:0;width:69px;height:192px;padding-top:44px;background:var(--blue)">
    <svg width="22" height="22" viewBox="0 0 22 22" fill="none" stroke="#fff" stroke-width="1"><circle cx="9" cy="9" r="6"/><path d="M13.5 13.5L20 20"/></svg>
    <h5 style="margin-top:34px">Heading Here</h5><p class="tiny" style="text-align:left">Describe this step in a few short and clear words for the audience.</p></div>
  <div class="feature" style="left:207px;top:0;width:69px;height:192px;padding-top:44px;background:var(--blue-2)">
    <svg width="22" height="22" viewBox="0 0 22 22" fill="none" stroke="#fff" stroke-width="1"><rect x="3" y="3" width="16" height="16"/><line x1="3" y1="7" x2="19" y2="7"/><circle cx="11" cy="13" r="3"/></svg>
    <h5 style="margin-top:34px">Heading Here</h5><p class="tiny" style="text-align:left">Describe this step in a few short and clear words for the audience.</p></div>
  <div class="feature" style="left:276px;top:0;width:68px;height:192px;padding-top:44px;background:var(--red)">
    <svg width="22" height="22" viewBox="0 0 22 22" fill="none" stroke="#fff" stroke-width="1"><circle cx="11" cy="11" r="9"/><circle cx="11" cy="11" r="5"/><circle cx="11" cy="11" r="2"/></svg>
    <h5 style="margin-top:34px">Heading Here</h5><p class="tiny" style="text-align:left">Describe this step in a few short and clear words for the audience.</p></div>
</section>

<section class="slide col-b row-4" aria-label="Mockup area with callouts">
  <h2 class="title">Our Mockup Area</h2>
  <div class="abs" style="left:0;right:0;top:112px;height:80px;background:var(--blue)"></div>
  <div class="abs" style="left:80px;top:33px;width:186px;height:124px;background:#1a1a1a;border-radius:5px"></div>
  <div class="abs" role="img" aria-label="Laptop screen" style="left:86px;top:39px;width:174px;height:110px;background:var(--white)"></div>
  <div class="abs" style="left:68px;top:156px;width:210px;height:4px;background:#c9cdd2;border-radius:0 0 4px 4px"></div>
  <div class="brand brand--red" style="left:130px;top:90px;font-size:6.5px"><span class="mark" style="width:6px;height:6px"></span>Copperleaf Studio</div>
  <svg class="abs" style="left:0;top:0" width="344" height="192" viewBox="0 0 344 192">
    <g stroke-width=".8" fill="none"><line x1="54" y1="68" x2="118" y2="68" stroke="#0a63c9"/><line x1="54" y1="96" x2="110" y2="96" stroke="#c0121f"/><line x1="54" y1="133" x2="95" y2="133" stroke="#111"/>
    <line x1="230" y1="68" x2="290" y2="68" stroke="#0a63c9"/><line x1="234" y1="96" x2="290" y2="96" stroke="#c0121f"/><line x1="220" y1="133" x2="290" y2="133" stroke="#111"/></g>
    <g><circle cx="118" cy="68" r="1.2" fill="#0a63c9"/><circle cx="110" cy="96" r="1.2" fill="#c0121f"/><circle cx="95" cy="133" r="1.2" fill="#111"/><circle cx="230" cy="68" r="1.2" fill="#0a63c9"/><circle cx="234" cy="96" r="1.2" fill="#c0121f"/><circle cx="220" cy="133" r="1.2" fill="#111"/></g>
  </svg>
  <div class="label" style="left:14px;top:62px;background:var(--blue)">Your Text<br>Goes Here</div>
  <div class="label" style="left:14px;top:90px;background:var(--red)">Your Text<br>Goes Here</div>
  <div class="label" style="left:14px;top:127px;background:var(--black)">Your Text<br>Goes Here</div>
  <div class="label" style="left:290px;top:62px;background:var(--blue)">Your Text<br>Goes Here</div>
  <div class="label" style="left:290px;top:90px;background:var(--red)">Your Text<br>Goes Here</div>
  <div class="label" style="left:290px;top:127px;background:var(--black)">Your Text<br>Goes Here</div>
</section>

<section class="slide col-c row-4" aria-label="Right picture slide with chart">
  <div class="abs" style="left:0;top:0;width:171px;height:192px;background:var(--blue)"></div>
  <div class="abs" style="left:44px;top:34px;width:96px;height:96px;border:2px solid var(--white);border-radius:50%;display:flex;align-items:center;justify-content:center;text-align:center;color:var(--white);font-size:12px;line-height:1.3">RIGHT<br>PICTURE<br>SLIDE</div>
  <p class="abs tiny" style="left:50px;top:140px;width:84px;text-align:center;color:var(--white)">Add a short caption for this picture here.</p>
  <svg class="abs" style="left:171px;top:0" width="173" height="192" viewBox="0 0 173 192">
    <g fill="#0a63c9"><rect x="14" y="46" width="4" height="52"/><rect x="47" y="64" width="4" height="34"/><rect x="80" y="60" width="4" height="38"/><rect x="113" y="40" width="4" height="58"/></g>
    <g fill="#c0121f"><rect x="20" y="70" width="4" height="28"/><rect x="53" y="46" width="4" height="52"/><rect x="86" y="72" width="4" height="26"/><rect x="119" y="62" width="4" height="36"/></g>
    <g fill="#111"><rect x="26" y="76" width="4" height="22"/><rect x="59" y="78" width="4" height="20"/><rect x="92" y="56" width="4" height="42"/><rect x="125" y="38" width="4" height="60"/></g>
    <g font-size="3" fill="#666" font-family="Maven Pro, sans-serif"><circle cx="52" cy="110" r="1.2" fill="#0a63c9"/><text x="55" y="111">Sales</text><circle cx="68" cy="110" r="1.2" fill="#c0121f"/><text x="71" y="111">Market</text><circle cx="86" cy="110" r="1.2" fill="#111"/><text x="89" y="111">Cost</text></g>
    <path d="M11 132l4-7 4 7z" fill="#c0121f"/>
  </svg>
  <div class="abs" style="left:190px;top:122px;font-size:18px;font-weight:600;color:var(--blue)">85%</div>
  <div class="abs" style="left:190px;top:146px;font-size:4px;color:var(--blue)">Profit</div>
  <p class="abs tiny" style="left:190px;top:153px;width:60px;color:var(--gray)">Short note on the result.</p>
</section>

<!-- Row 5 -->
<section class="slide col-a row-5" aria-label="Product mockup slide">
  <div class="photo" role="img" aria-label="Blue-tinted photo of office building windows" style="left:0;top:0;width:344px;height:94px;background:linear-gradient(135deg,#3a86dc,#0a5bbb 55%,#2a78d2)"></div>
  <div class="abs" style="left:16px;top:13px;font-size:12px;color:var(--white);text-transform:uppercase">Our Mockup</div>
  <div class="abs" style="left:8px;top:40px;font-size:7px;color:var(--white)">Heading Here</div>
  <p class="abs tiny" style="left:8px;top:50px;width:130px;color:var(--white)">Add a short line about this product view here for readers.</p>
  <div class="abs" style="left:12px;top:108px;width:9px;height:9px;border-radius:50%;background:var(--blue)"></div>
  <p class="abs tiny" style="left:28px;top:108px;width:115px;color:var(--gray)">Explain one key feature of the product in a short line.</p>
  <div class="abs" style="left:12px;top:138px;width:9px;height:9px;border-radius:50%;background:var(--red)"></div>
  <p class="abs tiny" style="left:28px;top:138px;width:115px;color:var(--gray)">Explain one key feature of the product in a short line.</p>
  <div class="abs" style="left:148px;top:16px;width:190px;height:122px;background:#161616;border-radius:4px"></div>
  <div class="abs" role="img" aria-label="Monitor screen" style="left:154px;top:22px;width:178px;height:104px;background:var(--white)"></div>
  <div class="abs" style="left:148px;top:130px;width:190px;height:10px;background:#d6d9dd"></div>
  <div class="abs" style="left:225px;top:140px;width:36px;height:18px;background:linear-gradient(#c4c8cd,#9ea4ab);clip-path:polygon(20% 0,80% 0,100% 100%,0 100%)"></div>
  <div class="brand brand--red" style="left:195px;top:70px;font-size:7px"><span class="mark" style="width:7px;height:7px"></span>Copperleaf Studio</div>
  <div class="foot"><div class="brand brand--red"><span class="mark"></span>Copperleaf Studio</div><div class="band"></div><span class="copy">© 2017 Copperleaf Studio. All rights reserved</span><span class="page">13</span></div>
</section>

<section class="slide col-b row-5" aria-label="Line chart slide">
  <div class="abs" style="left:22px;top:56px;font-size:12px;line-height:1.3;text-transform:uppercase">This is Line<br>Chart Slide</div>
  <div class="btn" style="left:24px;top:103px">CREATE TEXT HERE</div>
  <p class="abs tiny" style="left:28px;top:130px;width:82px;color:var(--gray)"><span style="color:var(--blue)">Describe the trend</span> shown in this chart with a short note.</p>
  <svg class="abs" style="left:0;top:0" width="344" height="192" viewBox="0 0 344 192">
    <g stroke="#e3e6ea" stroke-width=".4"><line x1="165" y1="47" x2="330" y2="47"/><line x1="165" y1="67.6" x2="330" y2="67.6"/><line x1="165" y1="88.2" x2="330" y2="88.2"/><line x1="165" y1="108.8" x2="330" y2="108.8"/><line x1="165" y1="129.4" x2="330" y2="129.4"/><line x1="165" y1="150" x2="330" y2="150" stroke="#bbb"/></g>
    <g font-size="3.2" fill="#888" font-family="Maven Pro, sans-serif" text-anchor="end"><text x="150" y="49">5</text><text x="150" y="59">4.5</text><text x="150" y="69">4</text><text x="150" y="80">3.5</text><text x="150" y="90">3</text><text x="150" y="100">2.5</text><text x="150" y="111">2</text><text x="150" y="121">1.5</text><text x="150" y="131">1</text><text x="150" y="142">0.5</text><text x="150" y="152">0</text></g>
    <g font-size="3.2" fill="#888" font-family="Maven Pro, sans-serif" text-anchor="middle"><text x="185" y="158">Category 1</text><text x="228" y="158">Category 2</text><text x="272" y="158">Category 3</text><text x="315" y="158">Category 4</text></g>
    <polyline points="185,61.4 228,98.5 272,77.9 315,57.3" fill="none" stroke="#0a63c9" stroke-width="1.4"/>
    <polyline points="185,100.6 228,59.4 272,112.9 315,92.3" fill="none" stroke="#c0121f" stroke-width="1.4"/>
  </svg>
  <div class="foot"><div class="brand brand--red"><span class="mark"></span>Copperleaf Studio</div><div class="band"></div><span class="copy">© 2017 Copperleaf Studio. All rights reserved</span><span class="page">14</span></div>
</section>

<section class="slide col-c row-5" aria-label="Picture and text grid">
  <h2 class="title">Your Title Goes Here</h2>
  <div class="photo" role="img" aria-label="Photo looking up at glass skyscrapers" style="left:24px;top:50px;width:98px;height:60px;background:linear-gradient(135deg,#e7ecf2,#9aa7b5 50%,#6b7683)"></div>
  <div class="cell cell--red" style="left:122px;top:50px;width:98px;height:60px"><h5>Heading Goes Here</h5><p class="tiny">Add a short point about this topic here for readers.</p></div>
  <div class="photo" role="img" aria-label="Photo of a tall tower against the sky" style="left:220px;top:50px;width:98px;height:60px;background:linear-gradient(135deg,#c9d7e6,#7f93a8 55%,#e4eaf0)"></div>
  <div class="cell cell--blue" style="left:24px;top:110px;width:98px;height:60px"><h5>Heading Goes Here</h5><p class="tiny">Add a short point about this topic here for readers.</p></div>
  <div class="photo" role="img" aria-label="Photo of skyscrapers in warm light" style="left:122px;top:110px;width:98px;height:60px;background:linear-gradient(160deg,#f4dcae,#b89067 50%,#5f6b7a)"></div>
  <div class="cell cell--black" style="left:220px;top:110px;width:98px;height:60px"><h5>Heading Goes Here</h5><p class="tiny">Add a short point about this topic here for readers.</p></div>
  <div class="foot"><div class="brand brand--red"><span class="mark"></span>Copperleaf Studio</div><div class="band"></div><span class="copy">© 2017 Copperleaf Studio. All rights reserved</span><span class="page">15</span></div>
</section>

<!-- Row 6 -->
<section class="slide col-a row-6" aria-label="About us slide">
  <div class="photo" role="img" aria-label="Blue-tinted photo of a glass footbridge" style="left:0;top:0;width:242px;height:184px;background:linear-gradient(90deg,#1d5da8,#6f9ed4 45%,#d5e4f3 75%,#9ebde0)"></div>
  <div class="abs" style="left:172px;top:42px;width:172px;height:110px;background:var(--blue);padding:22px 14px 0 20px;color:var(--white)">
    <div style="font-size:12px;text-transform:uppercase;position:relative">About Us<span style="position:absolute;left:0;bottom:-3px;width:20px;height:1.5px;background:var(--white)"></span></div>
    <p class="tiny" style="margin-top:10px">Share who we are, what we do and why clients choose to work with our team.</p>
    <p class="tiny" style="margin-top:4px">Add one more short line about our values and goals.</p>
  </div>
  <div class="foot"><div class="brand brand--red"><span class="mark"></span>Copperleaf Studio</div><div class="band"></div><span class="copy">© 2017 Copperleaf Studio. All rights reserved</span><span class="page">16</span></div>
</section>

<section class="slide col-b row-6" aria-label="Divider page with photo">
  <div class="photo" role="img" aria-label="Blue-tinted photo of industrial steel structure" style="inset:0;background:linear-gradient(135deg,#2f7dd6,#0a55b0 50%,#3a86d8 80%,#0d4f9e)"></div>
  <div class="brand brand--red" style="left:88px;top:96px;font-size:7px"><span class="mark" style="width:7px;height:7px"></span>Copperleaf Studio</div>
  <div class="abs cover-title" style="left:42px;top:130px;color:var(--white);font-size:14px;line-height:1.35">This is Your<br>Divider Page</div>
</section>

<section class="slide col-c row-6" aria-label="Quote area">
  <h2 class="title">Quote Area</h2>
  <div class="abs" style="left:0;right:0;top:42px;height:140px;background:var(--blue)"></div>
  <div class="photo" role="img" aria-label="Photo of a city skyline with twin towers" style="left:170px;top:42px;width:174px;height:140px;background:linear-gradient(90deg,var(--blue) 0%,#6f8fb4 30%,#b8c4d1 70%,#8d99a6 100%)"></div>
  <blockquote class="abs" style="left:18px;top:80px;font-size:6.5px;line-height:1.55;color:var(--white)">“ Coming together is a beginning.<br>Keeping together is progress.<br>Working together is success. ”</blockquote>
  <div class="abs" style="left:28px;top:118px;font-size:6.5px;color:var(--white)">- Harlan Foster -</div>
  <div class="foot"><div class="brand brand--red"><span class="mark"></span>Copperleaf Studio</div><div class="band"></div><span class="copy">© 2017 Copperleaf Studio. All rights reserved</span><span class="page">18</span></div>
</section>

</body>
</html>
```